One page front and back healthcare law brochure

Our small law firm provides legal services to businesses in the health care industry. We would like a single page 8.5x11 front and back brochure that highlights the services we offer. The intent of the brochure is to communicate our professionalism, high work quality, and depth of experience in healthcare law.
Target Market(s)
Doctors, Hospitals, Medical practices, Dental practices, Healthcare clinics, Healthcare tech companies, Healthcare entrepreneurs, Nurses, Med Spas, Pain Management Clinics, Weight Loss Clinics
Industry/Entity Type
Legal, Healthcare
Requirements
Nice to have
- Visually align with https://tovin.law/ and https://tovin.law/health-care/

```html
<!DOCTYPE html>
<html lang="en">
<head>
<meta charset="utf-8">
<title>Tovin Law – Healthcare Law Brochure</title>
<link rel="stylesheet" href="https://fonts.googleapis.com/css2?family=Jost:wght@400;500&family=Barlow+Semi+Condensed:wght@600;700&display=swap">
<style>
  :root {
    --backdrop: #e9eaec;
    --brand-blue: #1b4f9c;
    --deep-blue: #1552ae;
    --bright-blue: #1f7fd0;
    --sky: #9cc7dc;
    --sky-light: #cfe3ec;
    --accent-yellow: #f3e13a;
    --ink: #333a45;
    --paper: #f3f4f6;
    --white: #ffffff;
  }
  * { box-sizing: border-box; margin: 0; padding: 0; }
  html, body { width: 1200px; height: 792px; overflow: hidden; }
  body {
    background: var(--backdrop);
    font-family: "Jost", "Century Gothic", sans-serif;
    position: relative;
  }
  .page {
    position: absolute;
    top: 33px;
    width: 560px;
    height: 725px;
    overflow: hidden;
    box-shadow: 0 4px 14px rgba(0,0,0,.18);
  }
  .page--front { left: 25px; background: var(--paper); }
  .page--back { left: 615px; background: var(--deep-blue); }

  /* shared firm name */
  .firm { display: flex; align-items: center; gap: 8px; }
  .firm__square { width: 18px; height: 18px; background: var(--brand-blue); }
  .firm__name {
    font-family: "Jost", sans-serif; font-weight: 400; font-size: 24px;
    color: var(--brand-blue); line-height: 1;
  }

  /* FRONT */
  .front-hero {
    position: absolute; left: 0; top: 0; width: 560px; height: 300px;
    background: linear-gradient(90deg, var(--sky) 0%, var(--sky-light) 55%, #e4eef3 100%);
  }
  .front-hero__photo {
    position: absolute; right: 0; top: 0; width: 240px; height: 300px;
    background: linear-gradient(100deg, rgba(207,227,236,0) 0%, #eef2f5 35%, #dfe6ea 70%, #c9d6dd 100%);
  }
  .front-hero__firm { position: absolute; left: 18px; top: 26px; }
  .front-hero__title {
    position: absolute; left: 18px; top: 92px;
    font-family: "Barlow Semi Condensed", sans-serif; font-weight: 700; font-size: 13.5px;
    color: var(--accent-yellow); letter-spacing: .2px;
  }
  .front-hero__intro {
    position: absolute; left: 18px; top: 118px; width: 295px;
    font-size: 13px; line-height: 19.5px; color: var(--brand-blue);
  }
  .front-body {
    position: absolute; left: 0; top: 300px; width: 560px; height: 425px;
    padding: 22px 28px 0;
    text-align: center;
  }
  .front-body__heading {
    font-family: "Barlow Semi Condensed", sans-serif; font-weight: 700; font-size: 13.5px;
    color: var(--brand-blue); margin-bottom: 10px;
  }
  .front-body p {
    font-size: 11.4px; line-height: 16.4px; color: var(--ink); margin-bottom: 12px;
  }
  .lead {
    font-family: "Barlow Semi Condensed", sans-serif; font-weight: 700;
    color: var(--bright-blue); font-size: 13px;
  }

  /* BACK */
  .back-photo {
    position: absolute; left: 0; top: 0; width: 560px; height: 280px;
    background: radial-gradient(circle at 52% 48%, #cfe8f6 0%, #6f9bb4 22%, #4d5f6c 55%, #5b4a44 100%);
  }
  .back-firm {
    position: absolute; top: 300px; left: 0; width: 560px;
    display: flex; justify-content: center;
  }
  .back-firm .firm__square { background: var(--white); }
  .back-firm .firm__name { color: var(--white); }
  .back-columns {
    position: absolute; top: 355px; left: 24px; right: 24px; bottom: 20px;
    display: flex; gap: 20px;
  }
  .services { width: 255px; padding-right: 14px; border-right: 1px solid rgba(255,255,255,.35); }
  .why { flex: 1; text-align: right; }
  .section-title {
    font-family: "Barlow Semi Condensed", sans-serif; font-weight: 700;
    font-size: 15px; color: #8fd0ff; margin-bottom: 8px;
    display: flex; align-items: center; gap: 8px;
  }
  .services .section-title::after { content: ""; flex: 1; height: 1px; background: rgba(143,208,255,.6); }
  .why .section-title { justify-content: flex-end; font-size: 13px; }
  .item { margin-bottom: 11px; }
  .item__name {
    font-family: "Barlow Semi Condensed", sans-serif; font-weight: 700;
    font-size: 11px; color: var(--accent-yellow); margin-bottom: 2px;
  }
  .item__text { font-size: 8.6px; line-height: 11.6px; color: var(--white); }
  .contact { margin-top: 6px; color: var(--white); font-size: 8.8px; line-height: 13px; }
  .contact__phone {
    font-family: "Barlow Semi Condensed", sans-serif; font-weight: 700;
    font-size: 15px; color: var(--white); display: inline-flex; align-items: center; gap: 4px;
  }
  .contact svg { vertical-align: middle; }
</style>
</head>
<body>

<section class="page page--front" aria-label="Brochure front">
  <div class="front-hero">
    <div class="front-hero__photo" role="img" aria-label="Photo of a doctor in a white coat holding a red stethoscope, wearing a wristwatch"></div>
    <div class="front-hero__firm firm"><span class="firm__square"></span><span class="firm__name">Tovin Law</span></div>
    <h2 class="front-hero__title">YOUR TRUSTED PARTNER IN HEALTHCARE LAW</h2>
    <p class="front-hero__intro">At Tovin Law, our dedicated Healthcare Law Practice Group is committed to safeguarding the interests of healthcare businesses like yours. Our team understands the unique challenges of this highly regulated industry. We are experienced in navigating the complexities of healthcare law to protect your business, allowing you to focus on what you do best: delivering exceptional care.</p>
  </div>

  <div class="front-body">
    <h3 class="front-body__heading">PROTECTING &amp; HELPING YOUR BUSINESS GROW</h3>
    <p><span class="lead">Whether you’re</span> starting a new business or managing an established enterprise, the focus of your attention and energy is on developing and commercializing your practice, products, and/or services. Due to time constraints and the overwhelming amount of work your business requires, proper legal planning sometimes takes a back seat. We can help. Tovin Law seeks to relieve the stress and anxiety associated with unaddressed legal issues by handling these challenges and allowing our clients to focus on growing their companies.</p>
    <p><span class="lead">Our Healthcare Law practice</span> encompasses a wide range of services. We guide clients through the proper establishment of new businesses, and the myriad issues that arise as companies interact with the public, other companies, regulatory bodies, and the government. We help make sure businesses are correctly organized and comply with state and federal laws, rules, and regulations pertaining to raising capital, acquiring other businesses or assets, protecting patient information, complying with health law regulations and statutes, and adding and removing owners.</p>
    <p><span class="lead">Buying a healthcare</span> business, cementing a strategic partnership, and executing an exit event are all fraught with pitfalls and unexpected risks. When a deal or contract needs to get negotiated, documented, and closed - we excel. We fight to get the right deal terms for our clients and offer creative solutions to help navigate these minefields and achieve a successful result.</p>
    <p><span class="lead">We work</span> with all forms of businesses including partnerships, limited liability companies (LLCs), and corporations. Regardless of the type of business, it is imperative that the potential legal threats and obstacles the business may face are properly addressed.</p>
  </div>
</section>

<section class="page page--back" aria-label="Brochure back">
  <div class="back-photo" role="img" aria-label="Photo of a person touching a glowing digital healthcare interface with a heart and stethoscope icon surrounded by medical symbols"></div>

  <div class="back-firm">
    <div class="firm"><span class="firm__square"></span><span class="firm__name">Tovin Law</span></div>
  </div>

  <div class="back-columns">
    <div class="services">
      <h3 class="section-title">OUR SERVICES</h3>
      <div class="item">
        <div class="item__name">Medical Practices</div>
        <p class="item__text">Navigating the intricate landscape of healthcare regulations, regulatory compliance, and business legal issues. We ensure that your practice operates smoothly while avoiding costly legal pitfalls.</p>
      </div>
      <div class="item">
        <div class="item__name">Med Spas</div>
        <p class="item__text">Guiding med spas through confusing and ever-changing regulations, licensing, and compliance issues while ensuring their operations are legally sound.</p>
      </div>
      <div class="item">
        <div class="item__name">Medical Device Companies</div>
        <p class="item__text">Providing counsel on regulatory compliance, intellectual property, product liability, and contracts to help device manufacturers succeed in a competitive marketplace.</p>
      </div>
      <div class="item">
        <div class="item__name">Medical Software Companies</div>
        <p class="item__text">Addressing the unique legal needs of software companies in healthcare, including data privacy, cybersecurity, and regulatory compliance.</p>
      </div>
      <div class="item">
        <div class="item__name">Weight Loss and Pain Management Clinics</div>
        <p class="item__text">Offering guidance and support on compliance, licensing, and patient care and safety to ensure exceptional care while adhering to strict regulatory standards.</p>
      </div>
    </div>

    <div class="why">
      <h3 class="section-title">Why Choose Tovin Law?</h3>
      <div class="item">
        <div class="item__name">- Industry-Focused</div>
        <p class="item__text">Our deep understanding of the healthcare sector enables us to provide tailored legal solutions.</p>
      </div>
      <div class="item">
        <div class="item__name">- Experienced Team</div>
        <p class="item__text">Our HIPAA certified attorneys have extensive experience in healthcare law, delivering effective counsel and representation.</p>
      </div>
      <div class="item">
        <div class="item__name">- Proactive Approach</div>
        <p class="item__text">We anticipate challenges before they arise, providing strategic advice to safeguard your business.</p>
      </div>
      <div class="item">
        <div class="item__name">- Comprehensive Services</div>
        <p class="item__text">From compliance to drafting legal documents to dispute resolution, we offer end-to-end legal support for most healthcare law needs.</p>
      </div>
      <div class="item contact">
        <div class="item__name">- Contact Us Today</div>
        <div class="contact__phone">(704) 555-0148
          <svg width="12" height="12" viewBox="0 0 24 24" aria-hidden="true"><path fill="#f3e13a" d="M6.6 10.8a15 15 0 006.6 6.6l2.2-2.2c.3-.3.7-.4 1-.2 1.1.4 2.3.6 3.6.6.6 0 1 .4 1 1V20c0 .6-.4 1-1 1A17 17 0 013 4c0-.6.4-1 1-1h3.5c.6 0 1 .4 1 1 0 1.3.2 2.5.6 3.6.1.3 0 .7-.2 1z"/></svg>
        </div>
        <div>www.tovin.law | info@tovin.law
          <svg width="10" height="8" viewBox="0 0 20 14" aria-hidden="true"><rect x="1" y="1" width="18" height="12" fill="none" stroke="#f3e13a" stroke-width="2"/><path d="M1 1l9 7 9-7" fill="none" stroke="#f3e13a" stroke-width="2"/></svg>
        </div>
        <div>4180 Harbor Mill Road, Suite 210
          <svg width="8" height="10" viewBox="0 0 16 22" aria-hidden="true"><path fill="#f3e13a" d="M8 0a8 8 0 00-8 8c0 6 8 14 8 14s8-8 8-14a8 8 0 00-8-8zm0 11a3 3 0 110-6 3 3 0 010 6z"/></svg>
        </div>
        <div>Linden, NC, 28000</div>
      </div>
    </div>
  </div>
</section>

</body>
</html>
```